DLB / WLB

I need a business card for the owner of sister companies. Please see minimalist version of our old business card for just the Dalworth business. We need to now have a card that shows off both the Dalworth logo and the Willow Lane Builders logo. We would like the aesthetic to go well with our brand, and not differ greatly from our Dalworth cards. These companies are sister companies, there is not one parent company. Looking for a visually appealing design, but not sure if it should be diagonal or something to make it visually attractive... or just some other type of divider. We prefer white logos with a blue background. White transparent background png logos are attached. Please use blue background with hex code 566b7c. The person and contact information will be on the back side, and I can do that myself. We will NOT need to add the text for design-build-sales-installation.

```html
<!DOCTYPE html>
<html lang="en">
<head>
<meta charset="UTF-8">
<title>Dalworth + Co / Willow Lane Builders – Business Card</title>
<link rel="stylesheet" href="https://fonts.googleapis.com/css2?family=Montserrat:wght@400;500;600;700&display=swap">
<style>
  :root {
    --brand-blue: #566b7c;
    --card-white: #ffffff;
    --page-bg: #e4e6e8;
    --ink: #1f1f1f;
    --logo-white: #f2f5f7;
  }
  * { margin: 0; padding: 0; box-sizing: border-box; }
  html, body {
    width: 1200px;
    height: 874px;
    overflow: hidden;
  }
  body {
    background: var(--page-bg);
    font-family: "Montserrat", sans-serif;
    display: flex;
    flex-direction: column;
    align-items: center;
    justify-content: center;
    gap: 36px;
  }
  .card {
    width: 640px;
    height: 366px;
    border-radius: 26px;
    position: relative;
    box-shadow: 0 10px 24px rgba(0,0,0,0.12);
  }

  /* Front: Willow Lane Builders */
  .card-front {
    background: var(--brand-blue);
    display: flex;
    align-items: center;
    justify-content: center;
  }
  .wlb-mark {
    display: flex;
    align-items: center;
    gap: 18px;
  }
  .wlb-square {
    width: 34px;
    height: 34px;
    background: var(--logo-white);
  }
  .wlb-name {
    color: var(--logo-white);
    font-weight: 700;
    font-size: 34px;
    letter-spacing: 0.5px;
  }

  /* Back: Dalworth + Co contact side */
  .card-back {
    background: var(--card-white);
  }
  .dlb-mark {
    position: absolute;
    top: 58px;
    left: 0;
    right: 0;
    display: flex;
    flex-direction: column;
    align-items: center;
    gap: 16px;
  }
  .dlb-square {
    width: 110px;
    height: 110px;
    border: 10px solid var(--brand-blue);
  }
  .dlb-name {
    color: var(--brand-blue);
    font-weight: 600;
    font-size: 28px;
    line-height: 1.1;
    text-align: center;
  }
  .contact-row {
    position: absolute;
    left: 60px;
    right: 50px;
    bottom: 42px;
    display: flex;
    align-items: stretch;
  }
  .person {
    width: 210px;
    text-align: right;
    padding-right: 24px;
  }
  .person-name {
    color: var(--brand-blue);
    font-weight: 700;
    font-size: 23px;
  }
  .person-title {
    color: var(--ink);
    font-size: 14px;
    margin-top: 2px;
  }
  .divider {
    width: 1.5px;
    background: var(--brand-blue);
  }
  .contact-list {
    list-style: none;
    padding-left: 20px;
    display: flex;
    flex-direction: column;
    gap: 6px;
    color: var(--ink);
    font-size: 15px;
  }
  .contact-list li {
    display: flex;
    align-items: center;
    gap: 10px;
  }
  .contact-icon {
    width: 14px;
    height: 14px;
    fill: var(--brand-blue);
    flex: none;
  }
</style>
</head>
<body>

  <section class="card card-front" aria-label="Card front">
    <div class="wlb-mark">
      <span class="wlb-square"></span>
      <span class="wlb-name">Willow Lane Builders</span>
    </div>
  </section>

  <section class="card card-back" aria-label="Card back">
    <div class="dlb-mark">
      <span class="dlb-square"></span>
      <span class="dlb-name">dalworth+co<br>kitchen+bath</span>
    </div>

    <div class="contact-row">
      <div class="person">
        <p class="person-name">Marcus Ellery</p>
        <p class="person-title">Owner</p>
      </div>
      <span class="divider"></span>
      <ul class="contact-list">
        <li>
          <svg class="contact-icon" viewBox="0 0 24 24"><path d="M6.6 10.8a15.2 15.2 0 0 0 6.6 6.6l2.2-2.2a1 1 0 0 1 1-.25 11.4 11.4 0 0 0 3.6.57 1 1 0 0 1 1 1V20a1 1 0 0 1-1 1A17 17 0 0 1 3 4a1 1 0 0 1 1-1h3.5a1 1 0 0 1 1 1c0 1.25.2 2.45.57 3.6a1 1 0 0 1-.25 1z"/></svg>
          (555)214-7730
        </li>
        <li>
          <svg class="contact-icon" viewBox="0 0 24 24"><path d="M2 5h20v14H2z M2 5l10 8 10-8" /></svg>
          hello@dalworthco.com
        </li>
        <li>
          <svg class="contact-icon" viewBox="0 0 24 24"><circle cx="12" cy="12" r="10"/></svg>
          www.dalworthco.com
        </li>
      </ul>
    </div>
  </section>

</body>
</html>
```